Startup Web Design and Hosting Company Requiring Wow Brochure!

I am a web designer new to the business and need a format to market myself to local businesses. I have a website that defines clearly who I am and what I do. I need to carry this information onto an exciting, eye catching brochure. Please follow the general theme and layout of the website using vibrant colours. I would like to advertise the fact that I am a one stop shop - design, maintenance, hosting and full support. This brochure will communicate that a quality website starts at $499. Social media integration is an import feature to communicate on the brochure -facebook, twitter, linked in etc as well as SEO.
Website: www.lorindabask.ca
Updates
Project Deadline Extended
Reason: Several of the designs are very great and I would like some time to see a few last revisions before I make a final decision. Some really great talent here.
Target Market(s)
Small business not yet on the web. Too busy to take on the task or not knowledgeable in this area.
Industry/Entity Type
Shop
Look and feel
Each slider illustrates characteristics of the customer's brand and the style your logo design should communicate.

```html
<!DOCTYPE html>
<html lang="en">
<head>
<meta charset="utf-8">
<title>Web Design &amp; Hosting Brochure</title>
<link href="https://fonts.googleapis.com/css2?family=Oswald:wght@500;600&family=Archivo+Narrow:wght@400;700&display=swap" rel="stylesheet">
<style>
  :root {
    --page: #ffffff;
    --panel-top: #f4f4f4;
    --panel-bottom: #e4e4e4;
    --navy: #1d5c8a;
    --service-head: #1f5a86;
    --service-body: #8a8a8a;
    --red: #e4222b;
    --red-dark: #b5161d;
    --blue: #1ba8e2;
    --blue-dark: #0b6aab;
    --white: #ffffff;
    --photo-dark: #2b2c2c;
    --photo-mid: #4a4b4a;
    --photo-light: #9fc6e0;
  }
  html, body {
    margin: 0;
    padding: 0;
    overflow: hidden;
    background: var(--page);
  }
  .brochure {
    position: relative;
    width: 1200px;
    height: 868px;
    overflow: hidden;
    background: var(--page);
    font-family: "Archivo Narrow", "Arial Narrow", sans-serif;
  }
  .shapes {
    position: absolute;
    inset: 0;
  }
  .block {
    position: absolute;
    color: var(--white);
  }
  .block h2 {
    margin: 0;
    font-family: "Oswald", "Arial Narrow", sans-serif;
    font-weight: 600;
    text-transform: uppercase;
    line-height: 1;
    letter-spacing: 0;
  }
  .block p {
    margin: 0;
    font-size: 12.2px;
    line-height: 11.6px;
  }
  .about { left: 42px; top: 540px; width: 318px; }
  .about h2 { font-size: 31px; margin-bottom: 2px; }
  .about strong { font-weight: 700; }

  .offer { left: 418px; width: 352px; }
  .offer h2 { font-size: 34px; margin-bottom: 0; }
  .offer-design { top: 535px; }
  .offer-hosting { top: 641px; }
  .offer-support { top: 752px; }

  .services-title {
    position: absolute;
    left: 816px;
    top: 27px;
    margin: 0;
    font-family: "Oswald", "Arial Narrow", sans-serif;
    font-weight: 500;
    font-size: 44px;
    line-height: 1;
    color: var(--white);
    text-transform: uppercase;
  }
  .service {
    position: absolute;
    left: 816px;
    width: 348px;
  }
  .service h3 {
    margin: 0 0 1px;
    font-family: "Oswald", "Arial Narrow", sans-serif;
    font-weight: 500;
    font-size: 19px;
    line-height: 1;
    color: var(--service-head);
    text-transform: uppercase;
  }
  .service p {
    margin: 0;
    font-size: 11.6px;
    line-height: 11.6px;
    color: var(--service-body);
  }
</style>
</head>
<body>
<div class="brochure">
  <svg class="shapes" width="1200" height="868" viewBox="0 0 1200 868">
    <defs>
      <linearGradient id="panelFill" x1="0" y1="0" x2="0" y2="1">
        <stop offset="0" stop-color="var(--panel-top)"/>
        <stop offset="1" stop-color="var(--panel-bottom)"/>
      </linearGradient>
      <radialGradient id="photoFill" cx="0.5" cy="0.35" r="0.7">
        <stop offset="0" stop-color="var(--photo-light)"/>
        <stop offset="0.25" stop-color="var(--photo-mid)"/>
        <stop offset="1" stop-color="var(--photo-dark)"/>
      </radialGradient>
      <linearGradient id="redFill" x1="0" y1="0" x2="1" y2="1">
        <stop offset="0" stop-color="var(--red)"/>
        <stop offset="1" stop-color="var(--red-dark)"/>
      </linearGradient>
      <linearGradient id="blueFill" x1="0" y1="0" x2="1" y2="1">
        <stop offset="0" stop-color="var(--blue)"/>
        <stop offset="1" stop-color="var(--blue-dark)"/>
      </linearGradient>
    </defs>
    <rect x="793" y="15" width="390" height="840" fill="url(#panelFill)"/>
    <rect x="18" y="15" width="772" height="520" fill="url(#photoFill)" role="img" aria-label="Photo of a man facing a glowing keyhole doorway onto a road with an upward arrow, surrounded by chalkboard sketches about SEO, web traffic, social media and content"/>
    <path d="M18 548 Q18 533 40 531 L352 487 Q378 484 384 505 L415 855 L18 855 Z" fill="url(#redFill)"/>
    <path d="M352 538 Q348 520 372 516 L758 455 Q790 450 790 478 L790 855 L402 855 Z" fill="url(#blueFill)"/>
    <path d="M793 15 L1082 15 Q1094 15 1090 27 L1076 76 Q1072 88 1058 88 L793 88 Z" fill="var(--navy)"/>
  </svg>

  <section class="block about">
    <h2>Who am I?</h2>
    <p>I am a mother of two very strong and loving children, Maren and Tobias, and a wife to my soul mate and best friend, Derek. I started my career in the administrative and marketing fields in the space satellite and medical fields. Having started a family in 2003, I quickly realized that my heart was with my children and I couldn't possibly be in a better place than at home raising them. I spent the next 8 years with them, arranging their activities, bringing them to music lessons, dance lessons, art clubs… whatever they felt a passion for that made them even stronger children. In 2012, I decided it was time for me to return to work and I started my journey back into the workforce as a Virtual Assistant. There I learned intricacies of how to create a website using PressKit and realized my true passion was in the creativity of web design and delivering valuable websites to my clients. I now have a team of professionals who, along with me, deliver all the necessary components of web design, hosting, maintenance, and support. <strong>Thank you for making me part of your business and your lives.</strong></p>
  </section>

  <section class="block offer offer-design">
    <h2>Web Design</h2>
    <p>Creating cutting edge, custom website designs to support your business needs. More than just a website, an integrated web solution using the latest technologies to attract and maintain customers for our clients. Working with you to develop a design that reflects your company's vision.</p>
  </section>
  <section class="block offer offer-hosting">
    <h2>Hosting</h2>
    <p>Offering competitive hosting packages customized to suit your business needs. From multi-tenant to virtual private servers, we can help you choose the solution that best matches your requirements. We offer flexibility of control with your hosting package and even offer training to enable you to manage your site.</p>
  </section>
  <section class="block offer offer-support">
    <h2>Support</h2>
    <p>Our relationship does not end with the launch of your website. We are available to answer any questions or quickly resolve any issues to help you maintain and grow your online presence.</p>
  </section>

  <h2 class="services-title">Our Services</h2>

  <section class="service" style="top:117px">
    <h3>Responsive Design</h3>
    <p>We create websites that are fully responsive and can adapt to any screen size. Try resizing your browser window or view this page on your mobile device to see it happen.</p>
  </section>
  <section class="service" style="top:182px">
    <h3>Hosting Packages</h3>
    <p>Choose a package that's right for your business and pay for only what you need. Feeling a little "techy"? We can help you manage your own sites content with minimal training.</p>
  </section>
  <section class="service" style="top:248px">
    <h3>Maintenance</h3>
    <p>We have many maintenance options available that can accompany your web design package. Whether you need a little or a lot, we have a package that's right for you.</p>
  </section>
  <section class="service" style="top:312px">
    <h3>Support</h3>
    <p>Your website is finished, you're on your way! Our relationship doesn't end there. We're here for you with a continued relationship of support to help you through any concerns or issues you may have. Real people, fast and effective resolutions. That's our promise.</p>
  </section>
  <section class="service" style="top:386px">
    <h3>Domain Registration</h3>
    <p>We can find a domain name that suits your business quickly and securely. Set up can be completed in 24 hrs or less. We can transfer your existing domain name to our hosting service with minimal interruption. We offer PanelDesk controls to make your webserver simple enough for you to manage should you chose to. We can also manage your entire setup, install and maintenance. The choice is completely up to you.</p>
  </section>
  <section class="service" style="top:489px">
    <h3>Email Setup</h3>
    <p>Let us take the mystery out of email setup and configuration. Your package comes with unlimited email accounts on your domain. Email forwarders, spam protection, and ease of setup on any email app or device. We can walk you through the details or configuring your accounts and devices in minutes.</p>
  </section>
  <section class="service" style="top:566px">
    <h3>Newsletter</h3>
    <p>Keeping in touch with customers is a key factor in business success. A newsletter themed to match your website is a great way to keep customers and find new ones. Visitors to your site can sign up to your periodic publication to receive updates on your products, services or get free tips from you. A great way to stay in touch with your customers and we do all the heavy lifting.</p>
  </section>
  <section class="service" style="top:664px">
    <h3>Social Media Marketing</h3>
    <p>The results are in and Social Media is the fastest growing medium to reach new customers. We can integrate your current platforms into your website to gain acknowledgement and to let visitors connect with you via your social media. Not into social media? not to worry, we can get you up and running in days. We can even do your posting, tweeting and any other publishing you may need.</p>
  </section>
  <section class="service" style="top:758px">
    <h3>SEO</h3>
    <p>Search Engine Optimization, no need to panic. We can ensure your site and its collection of content are organized to meet search engine rules. Meta tags, headers, sitemap auto generation and submisssion, Searchly Webmaster Tools and Analytics, Searchly Authorship…we've got you covered. We make sure people can find you.</p>
  </section>
</div>
</body>
</html>
```